Outstanding Design for Australian Religious Network

Hello,

I am looking for a CSS theme design for an Australian pagan social network site based on the brelo platform, I have paid for the rights to customize the theme & layout design as I see fit. I am looking to completely customize its look, layout and coloring to bring needed potential to the site.

The domain still points to Brelo however this will soon be changed.

** Please note : The Current name is Heathcraft Downunder HOWEVER as we are updating the site we are updating the name and the name for the site will be The Hollow Lantern **

I would like the site to steer clear of the usual pagan imagery and would like the site to look like it has stepped back in time with an old antique look and old/traditional pagan imagery used for example . I would like the header to be quite large.

for example of old pagan images :

http://files.examplewiki.test/media/2/2d/Old_woodcut_scene.JPG

http://www.moonrakeblog.test/uploads/2010/03/old-engraving-hound.jpg

http://fernpathzine.test/images/2008/feature/Archive/figure.jpg

http://www.corvalinco.test/edge/figure1.gif

http://lanternnotes.blogsite.test/2007/02/figure1.jpg

http://www.moonrakeblog.test/uploads/2009/12/engraving706.jpg

I would like the theme to remain clean, crisp and modern with and old "feel"

I would like the colors to be more neutral and natural to keep with the old antiuqe feel however greens, browns, creams, and hints of bolder colors would be fine.

Please note I also like the idea of vines creeping in around the page if this is possible.

I like how the star is made out of twigs and vines.

http://www.tindlemarket.test/images/Sketch2.jpg

Essentially I would like to provide potential members with a unique experience when the enter the site, I would like the look to have a strong web presence that draws members in as if they are stepping back in time with the site.

For example the below pagan sites are the exact opposite of what I would like.

www.oakhearthring.test
www.emberkinhub.test

The site domain you will be working on is :

www.heathcraftdownunder.brelo.test

As you can see there is quite a clean slate to work with as the site is colorless and boring.

I would like to see how creative you can be as 90% percent of pagan site ( and there are millions ) are filled with boring graphic and bad gif's !!

I would like to be one of the first to provide a truly gratifying experience when the public land on this site.

This site was started as a personal endeavour into belief's and search for meaning, however from the day it was created people began to post and share and it has only continued to grow, I had questioned removing the site but the out cry I received from the participating members was huge and thus I decided to keep it running. Since that time all have agreed the site has so much potential however its look lets it down the most.In Australia paganism is still only coming out to be an everyday accepted religion and and I would like to continue to raise awareness and educate through The Hollow Lantern site.

Some examples of fully customized brelo sites are :

http://rally.dorvenfund.test/index.php

http://lumbrastone.brelo.test/

http://palettetricks.test/

http://schoolyardbuzz.test/
Updates

Project Deadline Extended
Reason: I am extending the deadline as I would rather wait and make sure I am happy with my product and there is a higher quality of work as it has not been as rushed.

Thank you again

Project Deadline Extended
Reason:

Project Deadline Extended
Reason: Awaiting a design

Target Market(s)

My target market is members of all ages 18 - 60 in western speaking countries, however I would like the site to be clear in its depiction of paganism and not using imagery that may offend.

Industry/Entity Type

Religious

Requirements
Must have
• The site look is the main priority, the are many unique users to the site everyday and this number has been increasing however it is let down by the overall look of the site. Brelo have a simple customization techniques that can altered via the site however they do little to improve the site to a level that it will meet its desired potential.
Nice to have
• On the top right of the site I would like buttons so members can easily connect with Chatterbook, quillr, Plunk.

```html
<!DOCTYPE html>
<html lang="en">
<head>
<meta charset="utf-8">
<title>Heathcraft Downunder</title>
<link href="https://fonts.googleapis.com/css2?family=Pirata+One&family=Crimson+Text:wght@700&family=Noto+Sans:wght@400;700&display=swap" rel="stylesheet">
<style>
:root{
  --bg:#eadbb9;
  --panel:#f7e7c8;
  --panel-edge:#d8c49e;
  --ink:#1d1408;
  --rule:#8c7a5a;
  --bar:#0d0a06;
  --bar-text:#f3e6c6;
  --gold-b:#e9cf7c;
  --white:#ffffff;
  --arrow:#2c7a1b;
}
*{box-sizing:border-box;margin:0;padding:0}
html,body{width:1162px;height:1200px;overflow:hidden;background:var(--bg)}
body{font-family:"Noto Sans",Verdana,sans-serif;color:var(--ink)}
.page{position:absolute;left:0;top:0;width:1002px;height:1035px;transform:scale(1.16);transform-origin:0 0;
  background:radial-gradient(ellipse at 50% 40%,#f1e4c6 0%,var(--bg) 70%,#dccaa3 100%)}
.abs{position:absolute}
.panel{position:absolute;background:var(--panel);border:1px solid var(--panel-edge)}
.bar{position:absolute;background:var(--bar);color:var(--bar-text);font-family:"Pirata One",serif;font-size:22px;padding:4px 12px;line-height:1}
.script{font-family:"Pirata One",serif;font-size:23px;color:var(--ink)}
.dotline{position:absolute;border-top:1px dotted var(--ink)}
.dashline{position:absolute;border-top:1px dashed var(--rule)}
.t-small{font-size:10.5px;line-height:14px}
.link{position:absolute;font-size:11px;font-weight:700}
.thumb{position:absolute;width:48px;height:48px}
.group-title{position:absolute;left:97px;font-size:11px;font-weight:700}
.group-count{position:absolute;left:99px;font-size:10.5px}
.group-sep{position:absolute;left:27px;width:205px;border-top:1px solid var(--panel-edge)}
.news{position:absolute;left:50px;width:170px;font-size:10.5px;line-height:14px}
.news::before{content:"";position:absolute;left:-12px;top:3px;border-left:6px solid var(--ink);border-top:4px solid transparent;border-bottom:4px solid transparent}
.news-sep{position:absolute;left:36px;width:192px;border-top:1px solid var(--panel-edge)}
.photo{position:absolute;width:152px;height:152px;background:var(--white);padding:6px}
.photo div{width:100%;height:100%}
.cap{position:absolute;width:152px;font-size:10.5px;line-height:14px}
.video-title{font-weight:700;font-size:10.5px}
.video{position:absolute;width:152px;height:116px;background:var(--bar)}
.video div{position:absolute;left:8px;top:20px;width:136px;height:76px}
.blog-item{position:absolute;left:769px;width:205px;height:87px;border-bottom:1px solid var(--panel-edge)}
.blog-icon{position:absolute;left:5px;width:32px;height:32px;background:linear-gradient(135deg,#e9a43a,#9c4d10)}
.blog-title{position:absolute;left:45px;font-size:11px;font-weight:700}
.blog-meta{position:absolute;left:45px;font-size:10.5px;line-height:14px}
.blog-stats{position:absolute;left:51px;font-size:11px;font-weight:700;word-spacing:28px}
.feed li{list-style:none;position:absolute;left:252px;width:497px;font-size:11px;font-weight:700;padding-left:10px}
.feed li::before{content:"";position:absolute;left:0;top:4px;border-left:6px solid var(--arrow);border-top:3.5px solid transparent;border-bottom:3.5px solid transparent}
.footer{position:absolute;left:25px;top:953px;width:950px;height:60px;
  background:linear-gradient(180deg,#b99339 0%,var(--gold-b) 45%,#c9a44b 100%);box-shadow:0 3px 6px rgba(60,40,10,.5)}
.footer span{position:absolute;top:25px;font-size:11.5px;font-weight:700}
</style>
</head>
<body>
<div class="page">

  <div class="panel" style="left:26px;top:-2px;width:207px;height:430px"></div>
  <div class="bar" style="left:29px;top:-8px;width:200px;height:28px;font-size:20px">Groups</div>
  <div class="thumb abs" style="left:39px;top:37px;background:linear-gradient(160deg,#c9c9c4,#2b2b2b)" role="img" aria-label="Group picture: figure in grey tones"></div>
  <div class="group-title" style="top:38px">SOLIATARY WITCH</div>
  <div class="group-count" style="top:58px">100 Members</div>
  <div class="group-sep" style="top:99px"></div>
  <div class="thumb abs" style="left:39px;top:119px;background:radial-gradient(circle,#4a4a2a,#050505)" role="img" aria-label="Group picture: dark cat"></div>
  <div class="group-title" style="top:120px">SOLIATARY WITCH</div>
  <div class="group-count" style="top:140px">100 Members</div>
  <div class="group-sep" style="top:181px"></div>
  <div class="thumb abs" style="left:39px;top:201px;background:linear-gradient(160deg,#8a7590,#c8b6b8)" role="img" aria-label="Group picture: robed figure"></div>
  <div class="group-title" style="top:202px">SOLIATARY WITCH</div>
  <div class="group-count" style="top:222px">100 Members</div>
  <div class="group-sep" style="top:263px"></div>
  <div class="thumb abs" style="left:39px;top:283px;background:radial-gradient(circle,#2a0808,#000)" role="img" aria-label="Group picture: dark mask"></div>
  <div class="group-title" style="top:284px">SOLIATARY WITCH</div>
  <div class="group-count" style="top:304px">100 Members</div>
  <div class="group-sep" style="top:345px"></div>
  <div class="thumb abs" style="left:39px;top:365px;background:radial-gradient(circle,#e0dde6,#6e6a80)" role="img" aria-label="Group picture: silver emblem"></div>
  <div class="group-title" style="top:366px">SOLIATARY WITCH</div>
  <div class="group-count" style="top:386px">100 Members</div>

  <div class="panel" style="left:26px;top:435px;width:207px;height:512px"></div>
  <div class="bar" style="left:29px;top:439px;width:200px;height:43px;padding-top:10px">The Ember Chase</div>
  <div class="news" style="top:491px">Anti-Native Sentiment Grows and other Pagan News of Note</div>
  <div class="news-sep" style="top:531px"></div>
  <div class="news" style="top:545px">Anti-Native Sentiment Grows and other Pagan News of Note</div>
  <div class="news-sep" style="top:585px"></div>
  <div class="news" style="top:598px">Anti-Native Sentiment Grows and other Pagan News of Note</div>
  <div class="news-sep" style="top:640px"></div>
  <div class="news" style="top:651px">Anti-Native Sentiment Grows and other Pagan News of Note</div>
  <div class="news-sep" style="top:692px"></div>
  <div class="news" style="top:702px">Anti-Native Sentiment Grows and other Pagan News of Note</div>
  <div class="news-sep" style="top:743px"></div>
  <div class="news" style="top:754px">Anti-Native Sentiment Grows and other Pagan News of Note</div>
  <div class="news-sep" style="top:796px"></div>
  <div class="news" style="top:809px">Anti-Native Sentiment Grows and other Pagan News of Note</div>
  <div class="news-sep" style="top:848px"></div>
  <div class="news" style="top:857px">Anti-Native Sentiment Grows and other Pagan News of Note</div>
  <div class="news-sep" style="top:896px"></div>
  <div class="news" style="top:904px">Anti-Native Sentiment Grows and other Pagan News of Note</div>

  <div class="panel" style="left:239px;top:-2px;width:522px;height:94px"></div>
  <div class="abs" style="left:256px;top:-14px;width:48px;height:48px;background:linear-gradient(135deg,#6d3c6e,#d6a58b)" role="img" aria-label="Organiser portrait"></div>
  <div class="abs" style="left:312px;top:-2px;font-family:'Crimson Text',serif;font-size:17px">MR.ALAN WESTBY</div>
  <div class="abs t-small" style="left:316px;top:24px">February 19, 2011 from 9:30am to 4pm – Amber Rites</div>
  <div class="abs" style="left:256px;top:47px;width:494px;border-top:1px solid var(--panel-edge)"></div>
  <div class="link" style="left:690px;top:59px">View All</div>

  <div class="panel" style="left:239px;top:94px;width:522px;height:334px"></div>
  <div class="script abs" style="left:257px;top:102px">Photos</div>
  <div class="dotline" style="left:316px;top:127px;width:434px"></div>
  <div class="photo" style="left:256px;top:148px"><div style="background:linear-gradient(180deg,#d6d6d8,#a9adb0 60%,#3c4236)" role="img" aria-label="Misty hillside photo"></div></div>
  <div class="photo" style="left:427px;top:148px"><div style="background:radial-gradient(circle at 55% 45%,#fff8d8,#8fa8c8 30%,#2c3e56 80%)" role="img" aria-label="Sunset over the sea photo"></div></div>
  <div class="photo" style="left:597px;top:148px"><div style="background:radial-gradient(circle at 50% 40%,#f4f7c6,#8fae2a 30%,#1e2a06 85%)" role="img" aria-label="Candle flame photo"></div></div>
  <div class="cap" style="left:257px;top:311px"><b>OUT AND ABOUT</b><br><b>Posted:</b> Still Brook<br>Added January 2, 2011 at<br>8:58am</div>
  <div class="cap" style="left:428px;top:311px"><b>OUT AND ABOUT</b><br><b>Posted:</b> by Still Brook<br>Added January 2, 2011 at<br>8:58am</div>
  <div class="cap" style="left:601px;top:311px"><b>OUT AND ABOUT</b><br><b>Posted:</b> by Still Brook<br>Added January 2, 2011 at<br>8:58am</div>
  <div class="dashline" style="left:257px;top:383px;width:491px"></div>
  <div class="link" style="left:263px;top:397px">Add Photos</div>
  <div class="link" style="left:695px;top:397px">View All</div>

  <div class="panel" style="left:239px;top:435px;width:522px;height:291px"></div>
  <div class="script abs" style="left:257px;top:445px">Videos</div>
  <div class="dotline" style="left:330px;top:469px;width:418px"></div>
  <div class="video" style="left:256px;top:485px"><div style="background:linear-gradient(135deg,#3a4bb0,#c01c3c)" role="img" aria-label="Video still: studio panel show"></div></div>
  <div class="video" style="left:427px;top:485px"><div style="background:linear-gradient(180deg,#9a9c98,#4a4a44)" role="img" aria-label="Video still: film scene"></div></div>
  <div class="video" style="left:597px;top:485px"><div style="background:linear-gradient(180deg,#6f7570,#343a34)" role="img" aria-label="Video still: crowd gathering"></div></div>
  <div class="cap" style="left:257px;top:607px"><span class="video-title">DRUIDS OFFICIAL ~ SATIRE<br>HOUR</span><br><b>Added:</b> Ashling</div>
  <div class="cap" style="left:428px;top:607px"><span class="video-title">DRUIDS OFFICIAL ~ SATIRE<br>HOUR</span><br><b>Added:</b> Ashling</div>
  <div class="cap" style="left:601px;top:607px"><span class="video-title">DRUIDS OFFICIAL ~ SATIRE<br>HOUR</span><br><b>Added:</b> Ashling</div>
  <div class="link" style="left:259px;top:658px">0</div><div class="link" style="left:344px;top:658px">0</div>
  <div class="link" style="left:433px;top:658px">0</div><div class="link" style="left:518px;top:658px">0</div>
  <div class="link" style="left:604px;top:658px">0</div><div class="link" style="left:688px;top:658px">0</div>
  <div class="dashline" style="left:257px;top:690px;width:491px"></div>
  <div class="link" style="left:263px;top:702px">Add Videos</div>
  <div class="link" style="left:695px;top:702px">View All</div>

  <div class="panel" style="left:239px;top:733px;width:522px;height:214px"></div>
  <div class="bar" style="left:244px;top:737px;width:512px;height:46px;font-size:28px;padding-top:9px">The Twilight Reel</div>
  <ul class="feed">
    <li style="top:803px">To Heal or Not to Heal: That Is the Question</li>
    <li style="top:829px">Missing an old friend</li>
    <li style="top:855px">History (not as wished for)</li>
    <li style="top:881px">You Too Can Make a Difference</li>
    <li style="top:907px">To Heal or Not to Heal: That Is the Question</li>
  </ul>
  <div class="dashline" style="left:249px;top:824px;width:503px"></div>
  <div class="dashline" style="left:249px;top:850px;width:503px"></div>
  <div class="dashline" style="left:249px;top:876px;width:503px"></div>
  <div class="dashline" style="left:249px;top:902px;width:503px"></div>
  <div class="dashline" style="left:249px;top:928px;width:503px"></div>

  <div class="panel" style="left:768px;top:-2px;width:207px;height:357px"></div>
  <div class="blog-item" style="top:-34px"><div class="blog-icon" style="top:34px" role="img" aria-label="Blogger avatar"></div><div class="blog-meta" style="top:34px">Posted by Hoodwright on<br>February 3, 2011 at 3:47am</div><div class="blog-stats" style="top:65px">3 1</div></div>
  <div class="blog-item" style="top:53px"><div class="blog-icon" style="top:12px" role="img" aria-label="Blogger avatar"></div><div class="blog-title" style="top:11px">Some Voodou Bits &amp; Pieces</div><div class="blog-meta" style="top:31px">Posted by Hoodwright on<br>February 3, 2011 at 3:47am</div><div class="blog-stats" style="top:66px">3 1</div></div>
  <div class="blog-item" style="top:140px"><div class="blog-icon" style="top:11px" role="img" aria-label="Blogger avatar"></div><div class="blog-title" style="top:10px">Some Voodou Bits &amp; Pieces</div><div class="blog-meta" style="top:30px">Posted by Hoodwright on<br>February 3, 2011 at 3:47am</div><div class="blog-stats" style="top:65px">3 1</div></div>
  <div class="blog-item" style="top:226px;border-bottom:none"><div class="blog-icon" style="top:12px" role="img" aria-label="Blogger avatar"></div><div class="blog-title" style="top:11px">Some Voodou Bits &amp; Pieces</div><div class="blog-meta" style="top:31px">Posted by Hoodwright on<br>February 3, 2011 at 3:47am</div><div class="blog-stats" style="top:66px">3 1</div></div>
  <div class="abs" style="left:776px;top:315px;width:190px;border-top:1px solid var(--panel-edge)"></div>
  <div class="link" style="left:777px;top:329px">Add A Blog Post</div>
  <div class="link" style="left:922px;top:329px">View All</div>

  <div class="panel" style="left:768px;top:362px;width:207px;height:416px"></div>
  <div class="bar" style="left:772px;top:367px;width:199px;height:36px;padding-top:7px">Sponsors</div>
  <div class="abs" style="left:776px;top:413px;width:191px;height:358px;background:var(--white);border:1px solid var(--panel-edge)"></div>
  <div class="abs" style="left:811px;top:433px;width:120px;height:150px;background:radial-gradient(circle at 50% 40%,#c8a35a,#5a3a1a 60%,#0d0a06)" role="img" aria-label="Partner badge"></div>
  <svg class="abs" style="left:797px;top:595px" width="150" height="160" viewBox="0 0 150 160" role="img" aria-label="Partner badge">
    <rect x="20" y="10" width="110" height="110" rx="6" fill="#0d0a06"/>
    <rect x="20" y="132" width="110" height="8" fill="#0d0a06"/>
    <rect x="40" y="148" width="70" height="5" fill="#0d0a06"/>
  </svg>

  <div class="footer">
    <span style="left:12px">© 2011&nbsp;&nbsp;heathcraftdownunder.test</span>
    <span style="left:675px">Badges&nbsp;&nbsp;|&nbsp;&nbsp;Report an Issue&nbsp;&nbsp;|&nbsp;&nbsp;Terms of Service</span>
  </div>

</div>
</body>
</html>
```